New Modern floristry business design

Hi, we are a new business based in Sydney called "copper fern floristry"

With so many floristry's we need a good design that will set a great first impression.

A few descriptive words on how we envision copper fern floristry:

-dynamic design
-minimal colour (colour can be used to enhance the design)
-black white grey (can include gold,silver,metallic shadowing)
Strong "COPPER FERN" with a classy "FLORISTRY"
Bold with a touch of feminine

Copper Fern Floristry,
Delia Varnet,
Copperfernfloristry@mailbay.com.au

```html
<!DOCTYPE html>
<html lang="en">
<head>
<meta charset="utf-8">
<title>Copper Fern Floristry – Business Card</title>
<link rel="stylesheet" href="https://fonts.googleapis.com/css2?family=Parisienne&family=Tinos&display=swap">
<style>
  :root {
    --stage: #d9d9d9;
    --stage-edge: #b5b5b5;
    --card-black: #0b0b0b;
    --pattern-dark: #141414;
    --pattern-mid: #262626;
    --band: #1b1b1b;
    --band-edge: #2c2c2c;
    --silver: #d8d8d8;
    --silver-soft: #a9a9a9;
    --grey-text: #8c8c8c;
  }
  * { margin: 0; padding: 0; box-sizing: border-box; }
  html, body {
    width: 1200px; height: 900px; overflow: hidden;
  }
  body {
    background: radial-gradient(ellipse at 50% 45%, var(--stage) 0%, var(--stage-edge) 100%);
    position: relative;
  }
  .card {
    position: absolute;
    left: 250px;
    width: 700px;
    height: 400px;
    background: var(--card-black);
    overflow: hidden;
    box-shadow: 0 14px 30px rgba(0,0,0,.35);
  }
  .card--back { top: 40px; }
  .card--front { top: 470px; }

  .pattern {
    position: absolute;
    inset: 0;
    background: radial-gradient(ellipse at 50% 45%, var(--pattern-mid) 0%, var(--pattern-dark) 55%, var(--card-black) 100%);
  }
  .card--front .pattern { bottom: 150px; }

  .tagline {
    position: absolute;
    left: 0; right: 0; top: 150px;
    text-align: center;
    font-family: "Parisienne", cursive;
    color: var(--silver-soft);
    font-size: 30px;
    line-height: 44px;
    letter-spacing: 1px;
  }

  .band {
    position: absolute;
    left: 0; right: 0;
    top: 235px; height: 95px;
    background: linear-gradient(180deg, var(--band-edge) 0%, var(--band) 12%, var(--band) 88%, var(--band-edge) 100%);
  }
  .base-stripe {
    position: absolute;
    left: 0; right: 0;
    top: 350px; height: 22px;
    background: linear-gradient(90deg, var(--card-black), #181818 50%, var(--card-black));
  }

  .brand {
    position: absolute;
    left: 0; right: 0; top: 150px;
    display: flex; align-items: center; justify-content: center; gap: 14px;
    font-family: "Tinos", serif;
    font-size: 40px;
    color: var(--silver);
    letter-spacing: 2px;
  }
  .brand-dot {
    width: 14px; height: 14px; border-radius: 50%;
    background: var(--silver);
  }

  .contact {
    position: absolute;
    left: 0; right: 0; top: 252px;
    text-align: center;
    font-family: "Tinos", serif;
    color: var(--grey-text);
  }
  .contact-name { font-size: 26px; line-height: 32px; color: var(--silver-soft); }
  .contact-email { font-size: 21px; line-height: 30px; }
</style>
</head>
<body>
  <section class="card card--back">
    <div class="pattern" role="img" aria-label="Dark damask floral swirl pattern"></div>
    <p class="tagline">for all your floristry needs....<br>Specialising in weddings and events</p>
  </section>

  <section class="card card--front">
    <div class="pattern" role="img" aria-label="Dark damask floral swirl pattern"></div>
    <div class="band"></div>
    <div class="base-stripe"></div>
    <div class="brand"><span class="brand-dot"></span><span>COPPER FERN FLORISTRY</span></div>
    <div class="contact">
      <p class="contact-name">Delia Varnet</p>
      <p class="contact-email">Copperfernfloristry@mailbay.com.au</p>
    </div>
  </section>
</body>
</html>
```